Infographic about product packaging for aged care

We need an infographic that will be published in Kestrel Magazine, to illustrate some points alongside our Aged Care feature.

Vector style preferred. Please incorporate bright blue and yellow into the colour scheme (Blue: 79C/28M/0Y/0K, Yellow: C5/M2/Y100/K0). Feel free to use other colours to supplement this palette.

Please use the image attached to this brief as a guide to colour and style. This is the opening page of the article.

Dimensions: 102mm x 102mm

Content:
- One in two Australians face difficulty opening or reading packaging
- 53 percent have suffered an injury as a result of inaccessible packaging.
- One in two people face at least one form of restriction:
o sensory (vision, hearing, taste)
o motion (strength, dexterity, locomotion, reach & stretch)
o cognitive (communication & understanding, intellectual functioning)

```html
<!DOCTYPE html>
<html lang="en">
<head>
<meta charset="utf-8">
<title>Packaging Accessibility – Kestrel Magazine Aged Care Feature</title>
<link rel="stylesheet" href="https://fonts.googleapis.com/css2?family=Oswald:wght@400;500;700&family=PT+Serif:wght@400&family=Roboto+Condensed:wght@700&display=swap">
<style>
  :root {
    --blue-light: #22dff2;
    --blue-mid: #16c3ee;
    --blue-deep: #1d8fe2;
    --yellow: #f5ef1a;
    --grey: #b3b5b5;
    --white: #ffffff;
    --rule: rgba(255, 255, 255, 0.85);
  }
  * { margin: 0; padding: 0; box-sizing: border-box; }
  html, body { width: 1200px; height: 1200px; overflow: hidden; }
  body {
    position: relative;
    background: linear-gradient(150deg, var(--blue-light) 0%, var(--blue-mid) 45%, var(--blue-deep) 100%);
    color: var(--white);
    font-family: "PT Serif", Georgia, serif;
  }
  .frame {
    position: absolute; left: 48px; top: 48px; width: 1104px; height: 1104px;
    border: 3px dotted var(--rule);
  }
  .rule-vertical {
    position: absolute; left: 568px; top: 48px; height: 620px;
    border-left: 3px dotted var(--rule);
  }
  .rule-horizontal {
    position: absolute; left: 48px; top: 720px; width: 1104px;
    border-top: 3px dotted var(--rule);
  }
  .people { position: absolute; }
  .people--large { left: 160px; top: 66px; width: 190px; height: 205px; }
  .people--small { left: 104px; top: 758px; width: 110px; height: 122px; }
  .stat-text {
    position: absolute; font-size: 45px; line-height: 1.02; letter-spacing: -0.5px;
  }
  .stat-text .num {
    font-family: "Roboto Condensed", "Oswald", sans-serif; font-weight: 700;
    font-size: 98px; line-height: 0.8; vertical-align: -2px;
  }
  .stat-one { left: 106px; top: 284px; width: 440px; }
  .stat-injury { left: 700px; top: 388px; width: 390px; }
  .stat-restriction { left: 104px; top: 902px; width: 330px; }
  .donut { position: absolute; left: 698px; top: 98px; width: 232px; height: 232px; }
  .donut-label {
    position: absolute; left: 698px; top: 98px; width: 232px; height: 232px;
    display: flex; align-items: center; justify-content: center;
    font-family: "Oswald", sans-serif; font-weight: 500; font-size: 66px;
  }
  .restriction-list { position: absolute; left: 430px; top: 760px; width: 700px; list-style: none; }
  .restriction {
    position: relative; padding-left: 108px; margin-bottom: 30px;
    font-size: 34px; line-height: 1.12; min-height: 104px;
  }
  .restriction-icon { position: absolute; left: 0; top: 0; width: 76px; height: 76px; }
  .restriction-name {
    font-family: "Oswald", sans-serif; font-weight: 400; font-size: 36px;
    color: var(--yellow); text-transform: uppercase; letter-spacing: 0.5px;
  }
  .restriction-name::before {
    content: ""; display: inline-block; width: 11px; height: 11px; border-radius: 50%;
    background: var(--white); margin-right: 12px; vertical-align: middle;
  }
  .icon-placeholder { border-radius: 50%; background: var(--yellow); }
</style>
</head>
<body>
  <div class="frame"></div>
  <div class="rule-vertical"></div>
  <div class="rule-horizontal"></div>

  <svg class="people people--large" viewBox="0 0 190 205" aria-hidden="true">
    <g fill="var(--grey)">
      <circle cx="140" cy="20" r="19"/>
      <rect x="112" y="46" width="56" height="76" rx="8"/>
      <rect x="119" y="110" width="18" height="95"/>
      <rect x="143" y="110" width="18" height="95"/>
    </g>
    <g fill="var(--yellow)">
      <circle cx="50" cy="20" r="19"/>
      <rect x="12" y="46" width="76" height="82" rx="10"/>
      <rect x="22" y="112" width="24" height="93"/>
      <rect x="54" y="112" width="24" height="93"/>
    </g>
  </svg>

  <p class="stat-text stat-one"><span class="num">1</span> in <span class="num">2</span> Australians face difficulty opening or reading packaging</p>

  <svg class="donut" viewBox="0 0 232 232" aria-hidden="true">
    <circle cx="116" cy="116" r="98" fill="none" stroke="var(--grey)" stroke-width="34"/>
    <circle cx="116" cy="116" r="98" fill="none" stroke="var(--yellow)" stroke-width="34"
            stroke-dasharray="326.3 615.8" transform="rotate(-90 116 116) scale(1 -1) translate(0 -232)"/>
  </svg>
  <div class="donut-label">53%</div>

  <p class="stat-text stat-injury">have suffered an injury as a result of inaccessible packaging</p>

  <svg class="people people--small" viewBox="0 0 190 205" aria-hidden="true">
    <g fill="var(--grey)">
      <circle cx="140" cy="20" r="19"/>
      <rect x="112" y="46" width="56" height="76" rx="8"/>
      <rect x="119" y="110" width="18" height="95"/>
      <rect x="143" y="110" width="18" height="95"/>
    </g>
    <g fill="var(--yellow)">
      <circle cx="50" cy="20" r="19"/>
      <rect x="12" y="46" width="76" height="82" rx="10"/>
      <rect x="22" y="112" width="24" height="93"/>
      <rect x="54" y="112" width="24" height="93"/>
    </g>
  </svg>

  <p class="stat-text stat-restriction"><span class="num">1</span> in <span class="num">2</span> face at least one form of restriction:</p>

  <ul class="restriction-list">
    <li class="restriction">
      <svg class="restriction-icon" viewBox="0 0 76 76" aria-hidden="true">
        <g fill="var(--yellow)">
          <circle cx="38" cy="38" r="12"/>
          <circle cx="38" cy="8" r="5"/><circle cx="38" cy="68" r="5"/>
          <circle cx="8" cy="38" r="5"/><circle cx="68" cy="38" r="5"/>
          <circle cx="17" cy="17" r="5"/><circle cx="59" cy="17" r="5"/>
          <circle cx="17" cy="59" r="5"/><circle cx="59" cy="59" r="5"/>
        </g>
      </svg>
      <span class="restriction-name">Sensory</span><br>(vision, hearing, taste)
    </li>
    <li class="restriction">
      <div class="restriction-icon icon-placeholder" role="img" aria-label="Hand icon representing motion"></div>
      <span class="restriction-name">Motion</span> (strength, dexterity, locomotion, reach &amp; stretch)
    </li>
    <li class="restriction">
      <div class="restriction-icon icon-placeholder" role="img" aria-label="Brain icon representing cognition"></div>
      <span class="restriction-name">Cognitive</span> (communication &amp; understanding, intellectual functioning)
    </li>
  </ul>
</body>
</html>
```